Car Wash - Total Redesign For New Owner - WIX or WordPress

Needs to be coded for WIX but will accept WordPress for outstanding designs.
This company has just been purchased and we now have a fresh logo to start off a totally new redesign of the web presence.
Sites I like:
https://www.vornelink.com.au/
https://www.qarrowtech.com/au-en/
http://plinthova.com/#homepage1
https://www.brelstondw.com.au/
What we sell can be found at the old website: www.glimmabaywa.com.au
The package names have changed. Current package names uploaded "Price List.jpg"
I like the product descriptions at https://www.brelstondw.com.au/
The new logo and prices have been uploaded. If it isn't on the price list, please don't carry it over from the old site.
The picture on the home page background should not be a car dashboard or an actual car wash. The image and the website will suggest luxury and having extra time to do things because you are not washing a car. Maybe you now have time to drive along a beautiful winding road by the sea? Or surprise me with an abstract background of colour or water droplets or something entirely different!
Please do something stunning that catches the eye. It must NOT look like I made it myself using a web building wizard.
Look at the websites I like - They will start you off.
Thanks and have fun!
Target Market(s)
We're selling a service that is geared for both male and females with higher incomes. They are 20-50 and usually have a car new car only a year or two old. They like nice ordered surroundings and a spotless car but don't have the time to clean it themselves.
Industry/Entity Type
Automotive
Requirements
Must have
- The theme is clean, easy to navigate but has a stunning visual impact.
- Online Bookings, Online Payment, Email Us
- Must look attractive and load quickly on mobile devices
- If you want a general idea of background image I think would be different for the home page, look at something similar to
- www.pixtorvale.com/pic-81264057/stock-photo-photo-of-water-splash-isolated-on-black.html?src=72kTzQmLpW8vHcnYdRsEBA-1-47 would do it.
- I'm not saying you have to use this picture. Just be aware I want something different. I want to grab people's attention with something a bit different.
Nice to have
- Very clean on the home page. Possibly a background of moving water or water drops. Close-ups of: clean car interiors; polished and glossy external surfaces. The home page does not have to have a picture but can be an abstract design, close up of an object or material (water or soap). If there is a picture on the home page, the theme must be about relaxation, luxury, beauty.
Should not have
- No before/after pictures on the home page.
- On the home page, do not use a picture where the specific model of car is obvious. It makes the website look too much like a car dealership!

```html
<!DOCTYPE html>
<html lang="en">
<head>
<meta charset="utf-8">
<title>Glimmabay WA – Automotive Detailing</title>
<link href="https://fonts.googleapis.com/css2?family=Ubuntu:wght@300;400;500;700&display=swap" rel="stylesheet">
<style>
:root{
  --blue:#0b8dd2;
  --blue-dark:#0a2f55;
  --title:#1a8fd0;
  --ink:#ffffff;
  --water-a:#0a3d6b;
  --water-b:#3fa7dc;
  --footer:#000000;
}
*{margin:0;padding:0;box-sizing:border-box}
html,body{width:745px;height:1200px;overflow:hidden;background:#fff;font-family:'Ubuntu',sans-serif;color:var(--ink)}
.page{position:relative;width:745px;height:1200px}
.water-bg{position:absolute;left:0;top:0;width:745px;height:363px;background:linear-gradient(180deg,#06182c 0,#0a2c4d 64px,var(--water-a) 64px,var(--water-b) 260px,#8fd0ef 363px)}
.brand{position:absolute;left:84px;top:18px;display:flex;align-items:center;gap:8px}
.brand-dot{width:30px;height:30px;border-radius:50%;background:var(--blue)}
.brand-name{font-weight:700;font-size:22px;color:#fff;letter-spacing:.5px}
.brand-tag{position:absolute;left:122px;top:47px;font-size:9px;color:#cfe6f5;font-weight:300}
.phone{position:absolute;left:543px;top:21px}
.phone small{display:block;font-size:7.5px;font-weight:400;color:#e8eef5}
.phone b{display:block;font-size:13px;font-weight:700;margin-top:3px}
.main-nav{position:absolute;left:82px;top:65px;width:581px;height:32px;background:var(--blue);display:flex;align-items:center;padding-left:22px;gap:16px;font-size:7.6px}
.hero{position:absolute;left:82px;top:97px;width:581px;height:245px;background:linear-gradient(110deg,#2b2f36 0,#4c4d3f 30%,#8a7a45 55%,#5d6b3a 75%,#2e3d2a 100%)}
.hero-caption{position:absolute;left:251px;top:98px;width:232px;height:116px;background:rgba(20,16,12,.82);padding:9px 16px}
.hero-caption h1{font-weight:400;font-size:20px;margin-bottom:8px}
.hero-caption p{font-size:6.3px;line-height:12px}
.hero-dots{position:absolute;left:636px;top:245px;display:flex;flex-direction:column;gap:9px}
.hero-dots i{width:6px;height:6px;border-radius:50%;background:#1b9be0;display:block}
.section-title{position:absolute;left:0;width:745px;text-align:center;font-size:16px;font-weight:500}
.prices-title{top:373px;color:var(--title)}
.card{position:absolute;background:var(--blue);width:261px}
.card h2{position:absolute;left:15px;top:9px;font-size:12px;font-weight:400}
.card ul{position:absolute;left:12px;top:33px;list-style:none;font-size:6.6px;line-height:12px;width:150px}
.card li{padding-left:12px;position:relative}
.card li::before{content:"";position:absolute;left:1px;top:4px;width:4px;height:4px;border:1px solid #fff;border-radius:50%}
.card li.note::before{display:none}
.rates{position:absolute;left:162px;top:33px;font-size:6.6px;line-height:12px}
.rates div{display:flex;width:82px;justify-content:space-between}
.btn{position:absolute;left:168px;bottom:10px;width:71px;height:21px;background:var(--blue-dark);font-size:7.2px;display:flex;align-items:center;justify-content:center}
.addon-head{position:absolute;left:164px;top:12px;font-size:7px;font-weight:700}
.addon-rates{position:absolute;left:162px;top:33px;font-size:6.6px;line-height:12px}
.about{position:absolute;left:0;top:720px;width:745px;height:192px;background:linear-gradient(160deg,#2f6f9a,#3f86b3 50%,#2d6b8c)}
.about h2{position:absolute;top:12px;width:100%;text-align:center;font-size:16px;font-weight:500}
.about p{position:absolute;left:158px;top:38px;width:430px;text-align:center;font-size:6.6px;line-height:12px}
.about .btn{left:337px;top:133px;bottom:auto;width:71px}
.map{position:absolute;left:0;top:912px;width:745px;height:192px;background:linear-gradient(135deg,#f3f1ea,#ebe8df 50%,#f3f1ea)}
.address{position:absolute;left:215px;top:30px;width:206px;height:78px;background:#fff;color:#666;font-size:10px;line-height:18px;padding:8px 12px 0 24px}
.address svg{position:absolute;left:10px;top:11px}
.footer{position:absolute;left:0;top:1104px;width:745px;height:96px;background:var(--footer)}
.footer-nav{position:absolute;top:22px;width:100%;display:flex;justify-content:center;gap:17px;font-size:7.6px}
.social{position:absolute;top:41px;width:100%;display:flex;justify-content:center;gap:10px}
.social i{width:21px;height:21px;border:1.5px solid #bbb;border-radius:50%;display:block}
.copy{position:absolute;top:76px;width:100%;text-align:center;font-size:6.6px;color:#aaa}
</style>
</head>
<body>
<div class="page">
  <div class="water-bg" role="img" aria-label="Blue water with droplets background"></div>

  <div class="brand"><span class="brand-dot"></span><span class="brand-name">Glimmabay WA</span></div>
  <div class="brand-tag">automotive detailing</div>
  <div class="phone"><small>FOR PHONE BOOKINGS, CALL</small><b>KAI: 0491 570 318</b></div>

  <nav class="main-nav"><span>HOME</span><span>OUR PACKAGES</span><span>OUR CLIENTS</span><span>OUR GALLERY</span><span>MAKE A BOOKING</span><span>FIND US</span></nav>

  <div class="hero" role="img" aria-label="Car driving fast along a tree-lined winding road">
    <div class="hero-caption">
      <h1>Glimmabay WA</h1>
      <p>At Glimmabay WA, there are two things we love the most; cars and attention to detail. That's what makes us the preferred car washing and detailing specialist among WA's leading car dealers and fleet companies, as well as the first choice among passionate motoring enthusiasts.</p>
    </div>
  </div>
  <div class="hero-dots"><i></i><i></i><i></i><i></i></div>

  <h2 class="section-title prices-title">PRICE LIST</h2>

  <div class="card" style="left:108px;top:400px;height:124px">
    <h2>MINI GLEAM</h2>
    <ul><li>Careful Hand Wash</li><li>Chamois Dry</li><li>Tyres Glossed</li><li>Interior Dusted</li><li>Vacuum</li></ul>
    <div class="rates"><div><span>SEDAN</span><span>$49</span></div><div><span>WAGON | SUV</span><span>$59</span></div><div><span>4WD | 7 SEATS</span><span>$79</span></div></div>
    <div class="btn">BOOK NOW</div>
  </div>

  <div class="card" style="left:376px;top:400px;height:124px">
    <h2>HALF GLEAM</h2>
    <ul><li>Mini Gleam Plus</li><li>Wheels and Door Jumbs Detailed</li><li>Interior Detail Upgrade</li></ul>
    <div class="rates"><div><span>SEDAN</span><span>$99</span></div><div><span>WAGON | SUV</span><span>$129</span></div><div><span>4WD | 7 SEATS</span><span>$159</span></div></div>
    <div class="btn">BOOK NOW</div>
  </div>

  <div class="card" style="left:108px;top:533px;height:149px">
    <h2>FULL GLEAM</h2>
    <ul><li>Half Gleam Plus</li><li>Full Interior Detail</li><li>Fabric Seat Shampoo</li><li>Carpets &amp; Mats Cleaned</li><li>Hand Polish</li><li class="note">(Excessive pet hair and / or Sand removal incurs addi-)</li></ul>
    <div class="rates"><div><span>SEDAN</span><span>$219</span></div><div><span>WAGON | SUV</span><span>$249</span></div><div><span>4WD | 7 SEATS</span><span>$279</span></div></div>
    <div class="btn">BOOK NOW</div>
  </div>

  <div class="card" style="left:376px;top:533px;height:149px">
    <h2>ALA CARTE ADD-ONS</h2>
    <div class="addon-head">SEDAN / SUV / 4WD</div>
    <ul><li>Fabric Seat Shampoo or Stain Removal</li><li class="note">(per seat)</li><li>Leather Seat Clean &amp; Conditioning</li><li class="note">(per seat)</li><li>Carpet Shampoo</li><li>Pet Hair &amp; Sand Vacuum Detail</li></ul>
    <div class="addon-rates"><div>$25</div><div>&nbsp;</div><div>$20</div><div>&nbsp;</div><div>$70 / $90 / $110</div><div>$40 / $60 / $80</div></div>
    <div class="btn">BOOK NOW</div>
  </div>

  <section class="about" role="img" aria-label="Coastal winding road through green hills with a blue tint">
    <h2>ABOUT US</h2>
    <p>We provide a range of service options to cater for the needs and budgets of our extensive and loyal customer base – from a simple wash through to a thorough detail, even scratch repairs. We even get the dirtiest 4WDs caked in red dust looking like new. With over 20 years experience, we adopt the very latest technologies, materials and techniques to help keep your much loved vehicle as shiny and new as the day you first met. As car enthusiasts, you'll rest assured knowing that your pride and joy is taken care of, all the way, by our highly skilled technicians.<br>And we're conveniently located close to the Marrowdale Train Station on Kestrel Beach Road in Fennick Park. You can leave your vehicle in our capable hands, do your own thing and collect it from us when it's ready. It's that simple.</p>
    <div class="btn">READ MORE</div>
  </section>

  <div class="map" role="img" aria-label="Street map of the business location">
    <div class="address">
      <svg width="9" height="12" viewBox="0 0 9 12"><path d="M4.5 0A4.5 4.5 0 0 0 0 4.5C0 8 4.5 12 4.5 12S9 8 9 4.5A4.5 4.5 0 0 0 4.5 0z" fill="#888"/><circle cx="4.5" cy="4.5" r="1.7" fill="#fff"/></svg>
      COMPANYNAME<br>1480 HARLOW FWY., SUITE 3120<br>DALLAS, TX 75207
    </div>
  </div>

  <footer class="footer">
    <nav class="footer-nav"><span>HOME</span><span>OUR PACKAGES</span><span>OUR CLIENTS</span><span>OUR GALLERY</span><span>MAKE A BOOKING</span><span>FIND US</span></nav>
    <div class="social"><i></i><i></i><i></i><i></i></div>
    <div class="copy">2016. www.companyname.com</div>
  </footer>
</div>
</body>
</html>
```